Business Card Design Project

Looking for a logo and business card for a Real State Business i will be opening. The name is not choosen yet , but will probably be RTV IMOVEIS.
I was thinking black and silver colors, but am open to nice ideas.
I did add a business card that i liked a lot, am looking for something like that, with logo in black or silver in a black card. The logo i was thinking in the letters RTV as i uploaded or something or little and cute buildings or a house...just ideas, can be any nice logo.
Updates

You guys can add other colors if you want, I like colors very "BRIGHT" and "open", like red, pink, strong colors. almost glow in the dark colors. lol

Designers,

I've increased more 88 dollars in the budget for 1st place cause I will want envelope designs... small and big sizes.

So 1st place is now U$248,00. 

No need to send the envelope designs right now... only the business cards designs.

Thank you.

Industry/Entity Type

Business

Requirements
Must have
• Renata Tavares Vilela

www.RTVimoveis-exemplo.com.br

+554188316402

renata@rtvimoveis-exemplo.com.br

```html
<!DOCTYPE html>
<html lang="pt-BR">
<head>
<meta charset="utf-8">
<title>RTV Imoveis – Cartões de visita</title>
<link rel="stylesheet" href="https://fonts.googleapis.com/css2?family=Open+Sans:wght@400;600&family=Berkshire+Swash&display=swap">
<style>
  :root {
    --page: #ffffff;
    --card: #0b0a07;
    --pink: #e0185c;
    --white: #ffffff;
    --ink: #111111;
  }
  * { box-sizing: border-box; margin: 0; padding: 0; }
  html, body { width: 1000px; height: 1200px; overflow: hidden; background: var(--page); }
  .sheet { position: relative; width: 1000px; height: 1200px; font-family: "Open Sans", Arial, sans-serif; }

  .variant-label {
    position: absolute; left: 74px; top: 42px;
    font-size: 54px; font-weight: 400; color: var(--ink); line-height: 1;
  }

  .card {
    position: absolute; left: 199px; width: 613px; height: 354px;
    background: var(--card); overflow: hidden;
  }
  .card--front { top: 45px; }
  .card--brand { top: 424px; }
  .card--full  { top: 801px; }

  /* Front card */
  .front-brand {
    position: absolute; left: 89px; top: 172px;
    font-size: 40px; font-weight: 600; color: var(--pink); letter-spacing: 1px; line-height: 1;
  }
  .divider {
    position: absolute; left: 236px; top: 58px; width: 3px; height: 238px; background: var(--pink);
  }
  .contact { position: absolute; left: 296px; top: 104px; color: var(--white); }
  .contact__name {
    font-family: "Berkshire Swash", cursive; font-size: 24px; color: var(--pink); line-height: 1.2;
    margin-bottom: 6px;
  }
  .contact__email { font-size: 17px; line-height: 1.3; }
  .contact__phone { font-size: 13px; line-height: 1.3; margin-top: 6px; }
  .contact__web   { font-size: 17px; line-height: 1.3; margin-top: 26px; }

  /* Brand-only card */
  .brand-mark {
    position: absolute; left: 0; right: 0; top: 125px; text-align: center;
    font-size: 112px; font-weight: 600; color: var(--pink); line-height: 1; letter-spacing: 2px;
  }

  /* Full name card */
  .brand-lockup {
    position: absolute; left: 0; right: 0; top: 140px; text-align: center;
    color: var(--white); font-weight: 600; line-height: 1;
  }
  .brand-lockup__letters { display: block; font-size: 96px; letter-spacing: 2px; }
  .brand-lockup__word { display: block; font-size: 30px; letter-spacing: 2px; margin-top: 4px; }
  .brand-accent {
    position: absolute; left: 294px; top: 100px; width: 26px; height: 26px; background: var(--pink);
  }
</style>
</head>
<body>
<main class="sheet">
  <div class="variant-label">A2</div>

  <section class="card card--front" aria-label="Frente do cartão">
    <div class="front-brand">RTV</div>
    <div class="divider"></div>
    <div class="contact">
      <p class="contact__name">Renata Tavares Vilela</p>
      <p class="contact__email">renata@rtvimoveis-exemplo.com.br</p>
      <p class="contact__phone">0055 418 831 6402</p>
      <p class="contact__web">www.RTVimoveis-exemplo.com.br</p>
    </div>
  </section>

  <section class="card card--brand" aria-label="Verso do cartão">
    <div class="brand-mark">RTV</div>
  </section>

  <section class="card card--full" aria-label="Verso alternativo do cartão">
    <div class="brand-accent"></div>
    <div class="brand-lockup">
      <span class="brand-lockup__letters">RTV</span>
      <span class="brand-lockup__word">IMOVEIS</span>
    </div>
  </section>
</main>
</body>
</html>
```